Yoga Instrucor

I need my personal business cards, i would like the front a kind of light but vibrant red and matt gold.

Industry/Entity Type

Business

Contact Information for Business Card

Rosalind Quenneby
Yoga Instructor
RYT 200, PRAVO (NYC) Yoga RYT 500,
CPR/ AED Certified,
quennebyrosalind@mailvista.net
512 804 6193
Adult Yoga, Private Yoga, Group Classes, Restorative, Meditation, Child Yoga.

```html
<!DOCTYPE html>
<html lang="en">
<head>
<meta charset="utf-8">
<title>Rosalind Quenneby – Yoga Instructor Business Cards</title>
<link rel="stylesheet" href="https://fonts.googleapis.com/css2?family=Italianno&family=Marcellus&family=Mulish:wght@700&display=swap">
<style>
  :root {
    --sheet: #ffffff;
    --wood-dark: #2e1309;
    --wood-mid: #4a2212;
    --wood-light: #5c2c17;
    --gold: #e2b146;
    --gold-bright: #f1c532;
    --gold-soft: #d7a64c;
    --lotus-core: #fff6c8;
    --lotus-mid: #f4d45a;
    --lotus-edge: #c9891f;
  }
  * { margin: 0; padding: 0; box-sizing: border-box; }
  html, body {
    width: 942px;
    height: 1200px;
    overflow: hidden;
    background: var(--sheet);
  }
  .sheet {
    position: relative;
    width: 942px;
    height: 1200px;
    background: var(--sheet);
  }
  .card {
    position: absolute;
    width: 817px;
    height: 467px;
    overflow: hidden;
    background:
      radial-gradient(ellipse 70% 60% at 50% 50%, rgba(120, 60, 30, 0.35), rgba(0, 0, 0, 0) 70%),
      linear-gradient(90deg, var(--wood-dark) 0%, var(--wood-mid) 30%, var(--wood-light) 50%, var(--wood-mid) 70%, var(--wood-dark) 100%);
  }
  .card--upper { left: 70px; top: 76px; }
  .card--lower { left: 68px; top: 626px; }

  .card__quote {
    position: absolute;
    left: 0;
    right: 0;
    top: 34px;
    text-align: center;
    font-family: "Italianno", cursive;
    font-size: 36px;
    line-height: 1;
    color: var(--gold-soft);
    letter-spacing: 0.2px;
  }
  .card__quote-author {
    position: absolute;
    right: 44px;
    top: 84px;
    font-family: "Italianno", cursive;
    font-size: 34px;
    line-height: 1;
    color: var(--gold-soft);
  }
  .card__lotus {
    position: absolute;
    left: 290px;
    top: 176px;
    width: 246px;
    height: 180px;
    border-radius: 50% 50% 46% 46% / 60% 60% 40% 40%;
    background: radial-gradient(ellipse at 50% 45%, var(--lotus-core) 0%, var(--lotus-mid) 45%, var(--lotus-edge) 85%, rgba(201, 137, 31, 0) 100%);
  }
  .card__credential {
    position: absolute;
    left: 38px;
    top: 260px;
    font-family: "Mulish", sans-serif;
    font-weight: 700;
    font-size: 29px;
    letter-spacing: 0.5px;
    color: var(--gold-bright);
  }
  .card__services {
    position: absolute;
    left: 40px;
    right: 30px;
    top: 376px;
    display: flex;
    justify-content: space-between;
    font-family: "Marcellus", serif;
    font-size: 23px;
    color: var(--gold);
    white-space: nowrap;
  }
  .card__divider { margin: 0 2px; }
</style>
</head>
<body>
<main class="sheet">
  <section class="card card--upper">
    <p class="card__quote">You are not a drop in the ocean. You are the entire ocean in a drop.</p>
    <p class="card__quote-author">- Oriel -</p>
    <div class="card__credential">PRAVO, RYT 500</div>
    <div class="card__lotus" role="img" aria-label="Glowing golden lotus flower illustration"></div>
    <p class="card__services">
      <span>Adult Yoga</span><span class="card__divider">|</span>
      <span>Group Classes</span><span class="card__divider">|</span>
      <span>Restorative</span><span class="card__divider">|</span>
      <span>Meditation</span><span class="card__divider">|</span>
      <span>Child Yoga</span>
    </p>
  </section>

  <section class="card card--lower">
    <p class="card__quote">You are not a drop in the ocean. You are the entire ocean in a drop.</p>
    <p class="card__quote-author">- Oriel -</p>
    <div class="card__credential">PRAVO, RYT 500</div>
    <div class="card__lotus" role="img" aria-label="Glowing golden lotus flower illustration"></div>
    <p class="card__services">
      <span>Adult Yoga</span><span class="card__divider">|</span>
      <span>Group Classes</span><span class="card__divider">|</span>
      <span>Restorative</span><span class="card__divider">|</span>
      <span>Meditation</span><span class="card__divider">|</span>
      <span>Child Yoga</span>
    </p>
  </section>
</main>
</body>
</html>
```